Design a Flooring flyer based on out information

We are a flooring company who specialise in supply & installation of high quality flooring (Laminate, SPC vinyl planks and engineered timber)

The colours in flyer should only consist the same colours in business logo as attached

Flyer needs to show customers we offer samples for free delivered to see quality and colours. This can only be ordered via our website.

Contact number: 1300 482 915

www.brantleyfloorcraft.com.au

instagram: brantleycraftcollective

Inregards to texts for flyer.. I will attach our body content of 'about us' Please add some key points in flyer

About Us

Marcus Brantley founded Brantley’s Floorcraft Group with one goal in mind – quality flooring equipment. Our team is made up of flooring professionals who have had extensive experience with flooring installation themselves. Therefore, we are experts at equipping customers with the right products they need to succeed.

The team at Brantley’s Floorcraft Group have had mastered all sorts of flooring technology as we are always focused on innovation and advancement. For example, our expert team has mastered the correct click system that floors need to be suitable for water spills, surface scratches, and foot traffic impact. This is just one of the ways our hands-on team strives to provide our customers with the innovative flooring technology.

Additionally, we make sure that our products are specifically suited to flourish in the Australian environment, and all of our equipment have been approved by Australian standards. Rain, drought or shine, our products are built to survive in Australian weather.

At Brantley’s Floorcraft Group, we work with you to ensure the best outcome for your unique situation. Just contact our friendly and knowledgeable team today to find out more.

Target Market(s)

Home owners

Requirements
Must have
• Logo colours, modern and expensive

```html
<!DOCTYPE html>
<html lang="en">
<head>
<meta charset="utf-8">
<title>Brantley's Floorcraft Group – Flooring Flyer</title>
<link href="https://fonts.googleapis.com/css2?family=Montserrat:wght@400;500;600;700;800&display=swap" rel="stylesheet">
<style>
  :root {
    --green: #7dc242;
    --green-dark: #5f9e2c;
    --charcoal: #444547;
    --slate: #6b6c6e;
    --ash: #9a9b9d;
    --paper: #ffffff;
    --ink: #4a4a4c;
  }
  * { box-sizing: border-box; margin: 0; padding: 0; }
  html, body { width: 866px; height: 1200px; overflow: hidden; background: var(--paper); }
  body { font-family: "Montserrat", sans-serif; color: var(--ink); }

  .flyer { position: relative; width: 866px; height: 1200px; overflow: hidden; background: var(--paper); }

  .hero-photo {
    position: absolute; left: 0; top: 0; width: 866px; height: 640px;
    background:
      linear-gradient(90deg, rgba(80,81,83,.92) 0%, rgba(100,101,103,.75) 38%, rgba(200,200,200,0) 62%),
      linear-gradient(160deg, #e9e8e4 0%, #d6d4cf 45%, #b9b7b2 100%);
  }

  .offer-strip {
    position: absolute; left: 0; top: 0; width: 866px; height: 58px;
    background: var(--charcoal); color: var(--paper);
    display: flex; align-items: center; justify-content: flex-end; padding-right: 34px;
    font-size: 19px; font-weight: 700; font-style: italic;
  }
  .offer-note {
    position: absolute; left: 230px; top: 58px; width: 636px; height: 38px;
    background: var(--green); color: var(--paper);
    display: flex; align-items: center; padding-left: 28px;
    font-size: 15px; font-weight: 600; letter-spacing: 1.5px; text-transform: uppercase;
  }

  .brand-box {
    position: absolute; left: 26px; top: 26px; width: 200px; height: 150px;
    background: var(--paper);
    display: flex; flex-direction: column; align-items: center; justify-content: center; gap: 12px;
    box-shadow: 0 4px 14px rgba(0,0,0,.18);
  }
  .brand-mark { width: 28px; height: 28px; background: var(--green); }
  .brand-name { font-size: 24px; font-weight: 700; color: var(--charcoal); letter-spacing: .5px; }

  .hero-copy { position: absolute; left: 40px; top: 300px; width: 560px; color: var(--paper); }
  .hero-question { font-size: 22px; font-weight: 600; line-height: 1.22; text-transform: uppercase; letter-spacing: .5px; }
  .hero-headline { margin-top: 22px; font-size: 42px; font-weight: 700; line-height: 1.15; }

  .call-tab {
    position: absolute; left: 0; top: 560px; width: 440px; height: 72px;
    background: var(--green); color: var(--paper);
    clip-path: polygon(0 0, 88% 0, 100% 100%, 0 100%);
    display: flex; align-items: center; padding-left: 40px;
    font-size: 34px; font-weight: 700;
  }

  .range-bar {
    position: absolute; left: 0; top: 632px; width: 866px; height: 66px;
    background: var(--charcoal); color: var(--paper);
    display: flex; align-items: center; padding-left: 40px; gap: 18px;
    font-size: 26px; font-weight: 600;
  }
  .range-divider { width: 2px; height: 30px; background: var(--paper); }

  .products { position: absolute; left: 40px; top: 722px; width: 786px; display: flex; gap: 18px; }
  .product { position: relative; flex: 1; height: 176px; overflow: hidden; }
  .product-photo { width: 100%; height: 100%; }
  .product-photo.laminate { background: linear-gradient(135deg, #f1f1ee 0%, #d9d2c6 55%, #b7aa96 100%); }
  .product-photo.spc { background: linear-gradient(120deg, #8d6e52 0%, #c6b29a 40%, #e0d6c8 70%, #6b5845 100%); }
  .product-photo.timber { background: linear-gradient(135deg, #c59a6b 0%, #e0bb8c 50%, #b3824f 100%); }
  .product-label {
    position: absolute; left: 0; bottom: 0; padding: 6px 14px;
    background: var(--green); color: var(--paper);
    font-size: 13px; font-weight: 700; text-transform: uppercase; letter-spacing: .5px;
  }
  .rule { position: absolute; left: 40px; top: 914px; width: 786px; height: 4px; background: var(--green); }

  .about { position: absolute; left: 40px; top: 936px; width: 540px; }
  .about-title { font-size: 24px; font-weight: 700; color: var(--charcoal); margin-bottom: 8px; }
  .about-list { list-style: none; }
  .about-list li { position: relative; padding-left: 24px; font-size: 12px; line-height: 1.45; margin-bottom: 7px; }
  .about-list li::before {
    content: ""; position: absolute; left: 0; top: 4px; width: 11px; height: 11px; background: var(--green);
  }

  .contact-box {
    position: absolute; left: 606px; top: 946px; width: 260px; height: 100px;
    background: var(--green); color: var(--paper);
    clip-path: polygon(10% 0, 100% 0, 100% 100%, 0 100%);
    display: flex; flex-direction: column; justify-content: center; padding-left: 34px; gap: 4px;
    font-size: 11.5px; font-weight: 600;
  }
  .contact-box .phone { font-size: 16px; font-weight: 700; }

  .closing-bar {
    position: absolute; left: 0; top: 1114px; width: 866px; height: 86px;
    background: var(--charcoal); color: var(--paper);
    display: flex; flex-direction: column; justify-content: center; padding: 0 40px; gap: 5px;
  }
  .closing-lead { font-size: 15px; font-weight: 600; font-style: italic; }
  .closing-cta { font-size: 13px; font-weight: 600; letter-spacing: 1px; text-transform: uppercase; }
</style>
</head>
<body>
<main class="flyer">
  <div class="hero-photo" role="img" aria-label="Smiling flooring installer in hard hat, plaid shirt and tool belt leaning on a white block wall beside stacked timber boards"></div>

  <div class="offer-strip">We offer samples for free delivered to see quality and colours</div>
  <div class="offer-note">This offer is only available via our website.</div>

  <div class="brand-box">
    <span class="brand-mark"></span>
    <span class="brand-name">BRANTLEY'S</span>
  </div>

  <div class="hero-copy">
    <p class="hero-question">Need a professional<br>flooring or tiling<br>installer?</p>
    <h1 class="hero-headline">We specialise in<br>supply &amp; installation<br>of high quality flooring</h1>
  </div>

  <div class="call-tab">Call:1300 482 915</div>

  <div class="range-bar">
    <span>Laminate</span><span class="range-divider"></span>
    <span>SPC Vinyl Planks</span><span class="range-divider"></span>
    <span>Engineered Timber</span>
  </div>

  <section class="products">
    <figure class="product">
      <div class="product-photo laminate" role="img" aria-label="Installer laying light laminate boards on underlay"></div>
      <figcaption class="product-label">Laminate</figcaption>
    </figure>
    <figure class="product">
      <div class="product-photo spc" role="img" aria-label="Fan of SPC vinyl plank colour samples"></div>
      <figcaption class="product-label">SPC Vinyl Planks</figcaption>
    </figure>
    <figure class="product">
      <div class="product-photo timber" role="img" aria-label="Herringbone engineered timber floor"></div>
      <figcaption class="product-label">Engineered Timber</figcaption>
    </figure>
  </section>
  <div class="rule"></div>

  <section class="about">
    <h2 class="about-title">About Us</h2>
    <ul class="about-list">
      <li>Marcus Brantley founded Brantley’s Floorcraft Group with one goal in mind – quality flooring equipment. Our team is made up of flooring professionals who have had extensive experience with flooring installation themselves.</li>
      <li>Our expert team has mastered the correct click system that floors need to be suitable for water spills, surface scratches, and foot traffic impact.</li>
      <li>We make sure that our products are specifically suited to flourish in the Australian environment, and all of our equipment have been approved by Australian standards. Rain, drought or shine, our products are built to survive in Australian weather.</li>
    </ul>
  </section>

  <aside class="contact-box">
    <span class="phone">Call:1300 482 915</span>
    <span>www.brantleyfloorcraft.com.au</span>
    <span>Instagram: brantleycraftcollective</span>
  </aside>

  <footer class="closing-bar">
    <p class="closing-lead">At Brantley’s Floorcraft Group, we work with you to ensure the best outcome for your unique situation.</p>
    <p class="closing-cta">Just contact our friendly and knowledgeable team today to find out more.</p>
  </footer>
</main>
</body>
</html>
```